Graphic Design Project

We make rose petal jelly from old fashioned english roses. The jelly is sweet eaten with scones and clotted cream or as a filling in a victoria sandwich, as a topping on ice cream or thick set yogurt.
The image of the product is luxurious and decadent and very english.
We need a design for a label which has a picture of an old fashioned rose (rosa mundi or a compte de chambard) The rose must stand out clearly so the jelly is not confused with other fruit jams. The overall colour of the label should be pink and soft, with white or dark pink writing. The label needs to be fridge proof.

We also need a security strip to fit on the lid of the jar.

We need the following information on the label.
Name of our company-"Petal Lantern"
Name of Product-"Rose Petal Jelly"
Sales pitch-"With whole petals-a taste of summer, delicious on scones, as a filling in sponge cake, as a topping on ice cream or yogurt."
INGREDIENTS: Sugar, water, rose petals, lemon juice, natural jelling agent (agar-agar)
STORAGE: Store in a cool dry place, once opened keep refrigerated and consume within 4 weeks.
BEST BEFORE: See base

200g
Produced by:
PETAL LANTERN
The Brambles
Marsh Lane
Ashcombe
Gloucestershire
GL19 4QT
The label must have room for a bar code. The size of label approx 8-10cm long 5cm wide.
Updates

Hi

Just been looking at the Greville and Hartley site and the labels they have there have the up market feel I am trying to convey. Hope that helps, its classy but not twee.

Thanks

Thanks for all submissions. I would be grateful if you googled images for 'Colourful and expensive biscuits at Greville Hartley' The designs on the tins are the image we are trying to create. The colours are quite strong.

Thanks

Target Market(s)

older well off people who visit garden centres

Industry/Entity Type

Security

Requirements
Must have
• All writen info above and picture of old fashioned rose prferably rose a mundi. Luxury feel, very english, to appeal to older market
Pink colour sheme
Should not have
• dark or manly colours

```html
<!DOCTYPE html>
<html lang="en">
<head>
<meta charset="utf-8">
<title>Rose Petal Jelly Label</title>
<link rel="stylesheet" href="https://fonts.googleapis.com/css2?family=Arimo:wght@400;700&family=Crimson+Text:ital@0;1&family=Marcellus+SC&display=swap">
<style>
  :root {
    --magenta: #c4197c;
    --magenta-deep: #b3146f;
    --cream: #fbf1e2;
    --cream-light: #fffdf8;
    --white: #ffffff;
    --ink: #1a1a1a;
    --rose-pink: #e7a3bd;
    --leaf-green: #8a9a6a;
  }
  html, body {
    margin: 0;
    padding: 0;
    overflow: hidden;
    background: var(--white);
  }
  .label {
    position: relative;
    width: 1200px;
    height: 666px;
    overflow: hidden;
    background: linear-gradient(90deg, var(--cream) 0%, var(--cream-light) 30%, var(--white) 55%, var(--cream-light) 80%, var(--cream) 100%);
    font-family: "Arimo", Arial, sans-serif;
  }
  .brand-tab {
    position: absolute;
    left: 350px;
    top: 0;
    width: 496px;
    height: 88px;
    background: var(--magenta);
    border-radius: 0 0 30px 30px;
    display: flex;
    align-items: center;
    justify-content: center;
    color: var(--white);
    font-family: "Marcellus SC", "Optima", serif;
    font-size: 34px;
    letter-spacing: 3px;
  }
  .rose-art {
    position: absolute;
    left: 0;
    top: 0;
    width: 258px;
    height: 480px;
    background: radial-gradient(ellipse at 45% 35%, var(--rose-pink) 0%, #f4d3df 40%, rgba(251,241,226,0) 75%),
                linear-gradient(180deg, rgba(138,154,106,0.25), rgba(231,163,189,0.3));
  }
  .product-name {
    position: absolute;
    left: 240px;
    width: 734px;
    top: 118px;
    margin: 0;
    text-align: center;
    color: var(--magenta);
    font-family: "Crimson Text", "Times New Roman", serif;
    font-weight: 400;
    font-size: 104px;
    line-height: 1;
  }
  .sales-pitch {
    position: absolute;
    left: 258px;
    width: 700px;
    top: 268px;
    margin: 0;
    text-align: center;
    color: var(--magenta);
    font-family: "Crimson Text", "Times New Roman", serif;
    font-style: italic;
    font-size: 32px;
    line-height: 48px;
  }
  .net-weight {
    position: absolute;
    left: 558px;
    width: 100px;
    top: 440px;
    text-align: center;
    color: var(--magenta);
    font-size: 26px;
  }
  .rule {
    position: absolute;
    left: 0;
    top: 480px;
    width: 1200px;
    height: 5px;
    background: var(--magenta);
  }
  .info-band {
    position: absolute;
    left: 0;
    top: 492px;
    width: 1200px;
    height: 174px;
    background: var(--magenta);
  }
  .product-details {
    position: absolute;
    left: 34px;
    top: 514px;
    margin: 0;
    color: var(--white);
    font-weight: 700;
    font-size: 21.5px;
    line-height: 32px;
  }
  .best-before {
    position: absolute;
    right: 233px;
    top: 574px;
    margin: 0;
    text-align: right;
    color: var(--white);
    font-weight: 700;
    font-size: 21.5px;
    line-height: 27px;
  }
  .producer-address {
    position: absolute;
    left: 1010px;
    top: 372px;
    width: 340px;
    margin: 0;
    transform: rotate(-90deg);
    transform-origin: 0 0;
    color: var(--magenta);
    font-style: normal;
    font-size: 24px;
    line-height: 34px;
    white-space: nowrap;
  }
  .barcode-space {
    position: absolute;
    left: 994px;
    top: 400px;
    width: 178px;
    height: 234px;
    box-sizing: border-box;
    background: var(--white);
    border: 2px solid var(--ink);
    display: flex;
    align-items: center;
    justify-content: center;
  }
  .barcode-space span {
    transform: rotate(90deg);
    color: var(--ink);
    font-size: 31px;
    line-height: 34px;
    text-align: center;
    white-space: nowrap;
  }
</style>
</head>
<body>
  <main class="label">
    <div class="rose-art" role="img" aria-label="Illustration of striped pink and white Rosa Mundi roses with leaves and buds"></div>

    <header class="brand-tab">Petal Lantern</header>

    <h1 class="product-name">Rose Petal Jelly</h1>

    <p class="sales-pitch">With whole petals - a taste of summer, delicious<br>on scones, as a filling in sponge cake,<br>as a topping on ice cream or yogurt.</p>

    <div class="net-weight">200g</div>

    <address class="producer-address">PETAL LANTERN<br>The Brambles, Marsh Lane,<br>Ashcombe, Gloucestershire<br>GL19 4QT</address>

    <div class="rule"></div>
    <section class="info-band"></section>

    <p class="product-details">INGREDIENTS: Sugar, water, rose petals, lemon juice,<br>natural jelling agent (agar-agar)<br>STORAGE: Store in a cool dry place, once opened keep<br>refrigerated and consume within 4 weeks.</p>

    <p class="best-before">BEST BEFORE:<br>See base</p>

    <div class="barcode-space"><span>BAR<br>CODE</span></div>
  </main>
</body>
</html>
```